New Business Card/Website Logo

We need a business card design for a new company based in Sydney. The company focuses mainly in construction in the field of form work and concreting. Attached is the logo being used already which can be used as a base for a new design, the current one is simply too bland and we are looking to spruce it up so it stands out and looks nicer. The logo would also be used on the website which is currently under construction. The attached image has the name, mobile and also the license number which needs to be there. The current email address on there can be removed and can be replaced with the website http://www.pillarvane.com.au, thanks!
Updates

Target Market(s)

Construction industry. Focusing on form work and concreting

Industry/Entity Type

Construction

Requirements
Must have
• License # on card along with website http://www.pillarvane.com.au and mobile phone number
Nice to have
• You have freedom with the design. The current design was a mock up done quite quickly. Please just keep in mind the target audience - construction, thanks.
Should not have
• the breezepost email address can be removed(refer picture) and replaced somewhere on the design with the website http://www.pillarvane.com.au

```html
<!DOCTYPE html>
<html lang="en">
<head>
<meta charset="utf-8">
<title>PillarVane Business Card</title>
<link rel="stylesheet" href="https://fonts.googleapis.com/css2?family=Exo+2:wght@600;700&display=swap">
<style>
  :root {
    --green: #5f9148;
    --green-dark: #2e4a22;
    --black: #000000;
    --white: #ffffff;
    --stage-light: #ffffff;
    --stage-grey: #cfd0d3;
    --stage-line: #d6d6d6;
    --type: "Exo 2", sans-serif;
  }
  * { margin: 0; padding: 0; box-sizing: border-box; }
  html, body { width: 1200px; height: 840px; overflow: hidden; }
  body { position: relative; background: var(--stage-light); font-family: var(--type); }

  .stage-lower {
    position: absolute; left: 0; top: 485px; width: 1200px; height: 355px;
    border-top: 1px solid var(--stage-line);
    background: linear-gradient(90deg, var(--stage-grey) 0%, #ecedee 38%, #ffffff 50%, #ecedee 62%, var(--stage-grey) 100%);
  }

  .card { position: absolute; overflow: hidden; background: var(--black); }
  .card--dark { left: 424px; top: 160px; width: 392px; height: 224px; }
  .card--split { left: 406px; top: 552px; width: 389px; height: 222px; background: var(--white); }

  .card__art { position: absolute; inset: 0; width: 100%; height: 100%; }

  .brand {
    position: absolute; left: 14px; top: 22px;
    display: flex; align-items: center; gap: 8px;
    color: var(--green); font-weight: 700; font-size: 22px; letter-spacing: 2px;
  }
  .brand__square { width: 18px; height: 18px; background: var(--green); }

  .identity { position: absolute; right: 12px; top: 11px; text-align: right; color: var(--white); font-weight: 600; }
  .card--split .identity { color: var(--green); }
  .identity__licence { font-size: 15px; line-height: 19px; }
  .identity__name { font-size: 16px; line-height: 24px; }

  .contact {
    position: absolute; right: 12px; bottom: 30px; text-align: right;
    color: var(--white); font-weight: 700; font-size: 14px; line-height: 20px;
  }
  .contact__phone { font-size: 16px; }
</style>
</head>
<body>
  <div class="stage-lower"></div>

  <section class="card card--dark">
    <svg class="card__art" viewBox="0 0 392 224" preserveAspectRatio="none" aria-hidden="true">
      <polygon points="0,224 392,118 392,224" fill="var(--green)"/>
      <polygon points="0,238 392,132 392,224 0,224" fill="var(--green-dark)"/>
      <polygon points="0,248 392,142 392,224 0,224" fill="var(--green)"/>
      <polygon points="0,262 392,156 392,224 0,224" fill="var(--green-dark)"/>
      <polygon points="0,272 392,166 392,224 0,224" fill="var(--green)"/>
      <polygon points="0,286 392,180 392,224 0,224" fill="var(--green-dark)"/>
      <polygon points="0,296 392,190 392,224 0,224" fill="var(--green)"/>
      <polygon points="0,310 392,204 392,224 0,224" fill="var(--green-dark)"/>
      <polygon points="0,320 392,214 392,224 0,224" fill="var(--green)"/>
    </svg>
    <div class="brand"><span class="brand__square"></span>PILLARVANE</div>
    <div class="identity">
      <p class="identity__licence">Licence: 348215C</p>
      <p class="identity__name">Mateo Sandoval</p>
    </div>
    <div class="contact">
      <p class="contact__phone">0412987563</p>
      <p>www.pillarvane.com.au</p>
    </div>
  </section>

  <section class="card card--split">
    <svg class="card__art" viewBox="0 0 389 222" preserveAspectRatio="none" aria-hidden="true">
      <polygon points="0,0 162,0 300,140 300,222 0,222" fill="var(--black)"/>
      <polygon points="0,222 389,117 389,222" fill="var(--green)"/>
      <polygon points="0,236 389,131 389,222 0,222" fill="var(--green-dark)"/>
      <polygon points="0,246 389,141 389,222 0,222" fill="var(--green)"/>
      <polygon points="0,260 389,155 389,222 0,222" fill="var(--green-dark)"/>
      <polygon points="0,270 389,165 389,222 0,222" fill="var(--green)"/>
      <polygon points="0,284 389,179 389,222 0,222" fill="var(--green-dark)"/>
      <polygon points="0,294 389,189 389,222 0,222" fill="var(--green)"/>
      <polygon points="0,308 389,203 389,222 0,222" fill="var(--green-dark)"/>
      <polygon points="0,318 389,213 389,222 0,222" fill="var(--green)"/>
    </svg>
    <div class="brand"><span class="brand__square"></span>PILLARVANE</div>
    <div class="identity">
      <p class="identity__licence">Licence: 348215C</p>
      <p class="identity__name">Mateo Sandoval</p>
    </div>
    <div class="contact">
      <p class="contact__phone">0412987563</p>
      <p>www.pillarvane.com.au</p>
    </div>
  </section>
</body>
</html>
```